Podiatry (services) Business Card

I need a business design for a New Podiatry Service.
the Podiatry services will include all aspects of podiatry including;
general podiatry for all ages
corns and callus treatment
Ingrown toenails & nail surgery
Forefoot, arch and heel pain
Gait analysis
Sports Podiatry and Orthotics
Paediatric Assessments
Diabetes Foot Assessment

I would like the back of the card to have space for next appointment day and time.

I would like a nice design that is simple yet catchy. I don't like cluttered business cards. I like things to be simple yet stand out because of the finer details.

I like the colours blue and white but I'm open to other designs that have different colours.

Industry/Entity Type

Business

Contact Information for Business Card

Cobaltline Podiatry (Business name)

Delphine Marrow - Podiatrist
M.Pod.P., B.Hlth. Sci, MQFodE

Address: 17 Tolbrook Rd, Ellerby Downs, 3187
Phone: (03) 9462 3178
Fax: (03) 9514 2683

```html
<!DOCTYPE html>
<html lang="en">
<head>
<meta charset="utf-8">
<title>Cobaltline Podiatry – Business Card</title>
<link rel="stylesheet" href="https://fonts.googleapis.com/css2?family=Marcellus&family=Noto+Serif:ital,wght@0,400;0,700;1,400&family=Open+Sans:wght@400&display=swap">
<style>
  :root {
    --cobalt: #3a5cb0;
    --cobalt-deep: #2f4f9f;
    --paper: #ffffff;
    --backdrop: #e9e4dc;
    --shadow: rgba(40, 30, 20, 0.28);
  }
  * { box-sizing: border-box; margin: 0; padding: 0; }
  html, body { width: 1200px; height: 952px; overflow: hidden; }
  body { background: var(--backdrop); position: relative; }

  .card {
    position: absolute;
    width: 620px;
    height: 354px;
    background: var(--paper);
    box-shadow: 0 10px 24px var(--shadow);
    overflow: hidden;
  }

  /* Front: brand panel with appointment strip */
  .card--front { left: 150px; top: 90px; }
  .front-panel {
    position: absolute; left: 0; top: 0; width: 100%; height: 278px;
    background: var(--cobalt);
    display: flex; align-items: center; justify-content: center; gap: 18px;
  }
  .brand-dot {
    width: 46px; height: 46px; border-radius: 50%;
    border: 3px solid var(--paper);
  }
  .brand-name {
    font-family: "Marcellus", serif;
    font-size: 44px;
    color: var(--paper);
    letter-spacing: 0.5px;
  }
  .appointment {
    position: absolute; left: 0; bottom: 0; width: 100%; height: 76px;
    font-family: "Open Sans", sans-serif;
    font-size: 15px; color: var(--cobalt);
  }
  .appointment__label { position: absolute; left: 92px; top: 14px; }
  .appointment__date { position: absolute; left: 160px; top: 36px; }
  .appointment__time { position: absolute; left: 348px; top: 22px; }

  /* Back: contact side */
  .card--back { left: 430px; top: 490px; }
  .back-shape { position: absolute; inset: 0; }
  .back-brand {
    position: absolute; left: 32px; top: 30px;
    display: flex; align-items: center; gap: 10px;
  }
  .back-brand .brand-dot {
    width: 26px; height: 26px; border: 2px solid var(--cobalt);
  }
  .back-brand .brand-name { font-size: 28px; color: var(--cobalt); }
  .back-brand-rule {
    position: absolute; left: 70px; top: 72px;
    width: 120px; height: 1px; background: var(--cobalt);
  }

  .contact {
    position: absolute; left: 300px; top: 128px;
    list-style: none;
    font-family: "Noto Serif", serif;
    font-size: 14px; line-height: 1.35;
    color: var(--cobalt-deep);
  }
  .contact li { display: flex; align-items: flex-start; gap: 8px; margin-bottom: 2px; }
  .contact svg { flex: none; width: 12px; height: 12px; margin-top: 3px; fill: var(--cobalt); }

  .practitioner {
    position: absolute; left: 50px; top: 262px; width: 250px;
    text-align: center;
    font-family: "Noto Serif", serif;
    color: var(--paper);
  }
  .practitioner__name { font-size: 20px; font-weight: 700; letter-spacing: 0.5px; }
  .practitioner__role { font-size: 14px; font-style: italic; letter-spacing: 1px; }
  .practitioner__credentials { font-size: 12.5px; font-weight: 700; margin-top: 4px; }
</style>
</head>
<body>

  <section class="card card--front">
    <div class="front-panel">
      <span class="brand-dot"></span>
      <span class="brand-name">Cobaltline Podiatry</span>
    </div>
    <div class="appointment">
      <span class="appointment__label">Next appointment,</span>
      <span class="appointment__date">Date ..................................</span>
      <span class="appointment__time">Time ................................</span>
    </div>
  </section>

  <section class="card card--back">
    <svg class="back-shape" viewBox="0 0 620 354" preserveAspectRatio="none" aria-hidden="true">
      <rect width="620" height="354" fill="var(--cobalt)"/>
      <path fill="var(--paper)" d="M0,0 H430 C540,0 600,60 600,140 C600,225 545,275 470,268 C400,262 340,212 230,204 C130,197 60,220 0,250 Z"/>
    </svg>

    <div class="back-brand">
      <span class="brand-dot"></span>
      <span class="brand-name">Cobaltline Podiatry</span>
    </div>
    <span class="back-brand-rule"></span>

    <ul class="contact">
      <li>
        <svg viewBox="0 0 12 12"><circle cx="6" cy="6" r="6"/><path d="M3.6 3.2l1.2-.4.8 1.6-.7.6c.3.7.8 1.2 1.5 1.5l.6-.7 1.6.8-.4 1.2c-2.6-.2-4.4-2-4.6-4.6z" fill="#fff"/></svg>
        <span>(03) 9462 3178</span>
      </li>
      <li>
        <svg viewBox="0 0 12 12"><circle cx="6" cy="6" r="6"/><rect x="3" y="3.8" width="6" height="4.4" fill="#fff"/><path d="M3 3.8l3 2.4 3-2.4" fill="none" stroke="#3a5cb0" stroke-width=".7"/></svg>
        <span>(03) 9514 2683</span>
      </li>
      <li>
        <svg viewBox="0 0 12 12"><path d="M6 0a4.2 4.2 0 0 0-4.2 4.2C1.8 7.4 6 12 6 12s4.2-4.6 4.2-7.8A4.2 4.2 0 0 0 6 0zm0 5.8a1.6 1.6 0 1 1 0-3.2 1.6 1.6 0 0 1 0 3.2z"/></svg>
        <span>17 Tolbrook Rd,<br>Ellerby Downs,<br>3187</span>
      </li>
    </ul>

    <div class="practitioner">
      <p class="practitioner__name">Delphine Marrow</p>
      <p class="practitioner__role">Podiatrist</p>
      <p class="practitioner__credentials">M.Pod.P., B.Hlth. Sci, MQFodE</p>
    </div>
  </section>

</body>
</html>
```